Etiketten für Bio Seifen
Zielgruppe
Wir stellen hochwertig 'handgemachte' Bio-Seifen her. Die Zielgruppe ist von 3-99 Jahren und zusätzlich haben wir auch noch Seife für Hunde.
Der Firmenname ist 'Kestrima'
Aufgabenstellung
Das Etikett soll Bezug auf Natur, Bio, Nachhaltigkeit nehmen. Wir stellen uns 'weiche' Aquarellfarben vor...Seife: Lavendel, Calendular, 7 Kräuter etc.
Das Etikett soll auf eine Beutelschachtel. Die Schachtel hat eine Anmaße: Breite 55mm; Höhe 120mm; Tiefe 30mm
Das Etikett soll im vorderen- und hinteren Bereich zusammenhängend geklebt werden.
Das Etikett soll eine Abmaße von: Breite 51mm; Höhe 114mm haben (Vorderseite) Rückseite gleich.
Wir möchten die Produkte auch gerne nummerieren, d.h. jede Seife hat eine Nummer die nicht zu groß dargestellt werden soll aber trotzdem gut leserlich.
Wir haben noch ein paar Bilder hochgeladen wie wir uns das ungefähr vorstellen.

```html
<!DOCTYPE html>
<html lang="de">
<head>
<meta charset="utf-8">
<title>Kestrima – Etiketten Bioseife</title>
<link href="https://fonts.googleapis.com/css2?family=Montserrat:wght@400;500&family=Playfair+Display:ital,wght@1,400;1,700&display=swap" rel="stylesheet">
<style>
  :root {
    --navy: #0e3b6c;
    --white: #ffffff;
    --trim: #c9c9c9;
    --lav-1: #5a3a86; --lav-2: #8a6bb0; --lav-3: #e6dcef;
    --cal-1: #f0a23a; --cal-2: #f7c46a; --cal-3: #fbe7bd;
    --herb-1: #1f8a4c; --herb-2: #5fb27a; --herb-3: #e3f1e4;
  }
  * { margin: 0; padding: 0; box-sizing: border-box; }
  html, body { width: 1200px; height: 786px; overflow: hidden; background: var(--white); }
  .sheet { position: relative; width: 1200px; height: 786px; }

  .label { position: absolute; top: 31px; width: 335px; height: 728px; border: 1px solid var(--trim); }
  .label--lavendel { left: 26px; }
  .label--calendula { left: 432px; }
  .label--kraeuter { left: 838px; }

  .label__art { position: absolute; left: 15px; top: 0; width: 304px; height: 698px; }
  .label--lavendel .label__art { background: linear-gradient(165deg, var(--lav-1) 0%, var(--lav-2) 45%, var(--lav-3) 100%); }
  .label--calendula .label__art { background: linear-gradient(165deg, var(--cal-2) 0%, var(--cal-1) 50%, var(--cal-3) 80%, var(--cal-2) 100%); }
  .label--kraeuter .label__art { background: linear-gradient(165deg, var(--herb-1) 0%, var(--herb-2) 45%, var(--herb-3) 100%); }

  .brand { position: absolute; left: 46px; top: 30px; width: 243px; height: 243px; background: var(--white); }
  .brand__frame { position: absolute; left: 0; top: 0; }
  .brand__name {
    position: absolute; left: 0; right: 0; top: 72px; text-align: center;
    font-family: "Montserrat", sans-serif; font-weight: 500; font-size: 42px;
    color: var(--navy); letter-spacing: 0.5px;
  }
  .brand__claim {
    position: absolute; left: 0; right: 0; top: 144px; text-align: center;
    font-family: "Playfair Display", serif; font-style: italic; font-size: 16px; color: var(--navy);
  }
  .brand__band {
    position: absolute; left: 9px; width: 225px; top: 205px; height: 29px;
    background: var(--navy); color: var(--white);
    font-family: "Montserrat", sans-serif; font-size: 14px; letter-spacing: 0.6px;
    display: flex; align-items: center; justify-content: center;
  }

  .fold { position: absolute; left: 15px; width: 304px; top: 304px; border-top: 1px dashed rgba(255,255,255,0.85); }

  .variant {
    position: absolute; left: 47px; top: 335px; width: 241px; height: 107px;
    background: var(--white); border: 2px solid var(--navy); border-radius: 5px;
    text-align: center; color: var(--navy);
  }
  .variant::before {
    content: ""; position: absolute; inset: 3px; border: 1px solid var(--navy); border-radius: 3px;
  }
  .variant__no { margin-top: 13px; font-family: "Montserrat", sans-serif; font-size: 16px; }
  .variant__name { margin-top: 2px; font-family: "Playfair Display", serif; font-style: italic; font-weight: 700; font-size: 21px; letter-spacing: 1.5px; }
  .variant__effect { margin-top: 4px; font-family: "Montserrat", sans-serif; font-size: 14px; }
</style>
</head>
<body>
<main class="sheet">

  <section class="label label--lavendel">
    <div class="label__art" role="img" aria-label="Lila Aquarellfläche mit weißen Blütenlinien"></div>
    <div class="brand">
      <svg class="brand__frame" width="243" height="243" aria-hidden="true">
        <polyline points="88,9 234,9 234,72" fill="none" stroke="var(--navy)" stroke-width="1.5"/>
        <polyline points="10,130 10,197 234,197 234,130" fill="none" stroke="var(--navy)" stroke-width="1.5"/>
      </svg>
      <div class="brand__name">Kestrima</div>
      <div class="brand__claim">Natur auf der Haut</div>
      <div class="brand__band">HANDGEMACHTE BIOSEIFE</div>
    </div>
    <div class="fold"></div>
    <div class="variant">
      <div class="variant__no">N°1</div>
      <div class="variant__name">LAVENDEL</div>
      <div class="variant__effect">beruhigend &amp; entspannend</div>
    </div>
  </section>

  <section class="label label--calendula">
    <div class="label__art" role="img" aria-label="Orange-gelbe Aquarellfläche mit weißen Blütenlinien"></div>
    <div class="brand">
      <svg class="brand__frame" width="243" height="243" aria-hidden="true">
        <polyline points="88,9 234,9 234,72" fill="none" stroke="var(--navy)" stroke-width="1.5"/>
        <polyline points="10,130 10,197 234,197 234,130" fill="none" stroke="var(--navy)" stroke-width="1.5"/>
      </svg>
      <div class="brand__name">Kestrima</div>
      <div class="brand__claim">Natur auf der Haut</div>
      <div class="brand__band">HANDGEMACHTE BIOSEIFE</div>
    </div>
    <div class="fold"></div>
    <div class="variant">
      <div class="variant__no">N°2</div>
      <div class="variant__name">CALENDULA</div>
      <div class="variant__effect">mild reinigend &amp; pflegend</div>
    </div>
  </section>

  <section class="label label--kraeuter">
    <div class="label__art" role="img" aria-label="Grüne Aquarellfläche mit weißen Blütenlinien"></div>
    <div class="brand">
      <svg class="brand__frame" width="243" height="243" aria-hidden="true">
        <polyline points="88,9 234,9 234,72" fill="none" stroke="var(--navy)" stroke-width="1.5"/>
        <polyline points="10,130 10,197 234,197 234,130" fill="none" stroke="var(--navy)" stroke-width="1.5"/>
      </svg>
      <div class="brand__name">Kestrima</div>
      <div class="brand__claim">Natur auf der Haut</div>
      <div class="brand__band">HANDGEMACHTE BIOSEIFE</div>
    </div>
    <div class="fold"></div>
    <div class="variant">
      <div class="variant__no">N°3</div>
      <div class="variant__name">7 KRÄUTER</div>
      <div class="variant__effect">nährend &amp; beruhigend</div>
    </div>
  </section>

</main>
</body>
</html>
```